Real Estate Site Update - wordpress

my wordpress site has not been updated in 6 years and needs a makeover
1. I would like to include my new logo (attached)
2. I would also like to include new staff photos (attached)
3. I would like to include client video testimonials (attached)
4. I would like to have real estate agent bio template pages for current and new agents
5. the site needs mobile device functionality
6. I would like a new look and more overall usability and functionality
Pages needed
1. main page
2. about us page
3. agent bio page template
4. 1st time buyer class sign up page - handbook purchase (coinvale)
5. property search pages (lotfinder hub)
6. first time buyer picture and announcement blog page
7. buyer information resources
8. seller information resources
I am looking for interesting Ideas on how to make my real estate website POP
current page is brightkeyhaven.com
I currently have and need
1. ability to post to social media (Activated)
2. I'd like to incorporate my youtube page brightkeyhavenny
3. ability to register clients for class attendance (activated need presentation update)
4. ability to charge for class and booklets via coinvale (activated)
5. ability to provide mls listing searches via lotfinderhub activated needs better presentation
if access to my current website file structure will assist please advise, i will gladly provide access
wordpress tools currently activated
QTRV
Pour Along
Lockmoat
Tablekit
Snipo
Lotfinder Hub
ages 22-50 income 30k and up
Real Estate

```html
<!DOCTYPE html>
<html lang="en">
<head>
<meta charset="utf-8">
<title>Brightkey Haven — Find Your Home</title>
<link rel="stylesheet" href="https://fonts.googleapis.com/css2?family=Raleway:wght@300;400;500;600;700&family=Open+Sans:wght@400;600&display=swap">
<style>
:root{
  --pink:#e0506e;
  --pink-dark:#c83d5b;
  --navy:#1b222c;
  --navy-deep:#141a22;
  --ink:#1e1e1e;
  --body:#333;
  --muted:#8a8f96;
  --light:#e9eaec;
  --white:#fff;
  --overlay:rgba(20,24,30,.55);
  --field:#fff;
}
*{box-sizing:border-box;margin:0;padding:0}
html,body{width:1200px;height:3046px;overflow:hidden}
body{position:relative;background:var(--white);font-family:"Open Sans",Arial,sans-serif;color:var(--body)}
.abs{position:absolute}

/* header + hero */
.hero{left:0;top:0;width:1200px;height:800px;
  background:linear-gradient(180deg,#9fb0b8 0%,#c9cfcc 22%,#7d8b7a 45%,#4f7a35 62%,#6fa043 80%,#5e8d35 100%)}
.site-header{left:0;top:0;width:1200px;height:116px;background:var(--overlay)}
.brand{left:56px;top:34px;font-family:"Raleway",sans-serif;font-weight:600;font-size:26px;color:var(--pink);letter-spacing:.5px}
.brand-mark{left:56px;top:70px;width:10px;height:10px;background:var(--pink)}
.main-nav{right:56px;top:38px;display:flex;gap:26px;align-items:center;font-family:"Raleway",sans-serif;font-weight:600;font-size:15px;color:var(--white)}
.main-nav .active{color:var(--pink)}
.btn-login{background:var(--pink);color:var(--white);padding:7px 14px}
.header-social{right:56px;top:101px;display:flex;gap:4px}
.header-social span{width:20px;height:20px;background:#2d6fb3}

.search-panel{left:350px;top:430px;width:505px;height:226px;background:rgba(25,28,33,.78)}
.panel-social{left:700px;top:408px;display:flex;gap:4px}
.panel-social span{width:40px;height:36px;background:#2d6fb3}
.search-title{left:378px;top:452px;font-family:"Raleway",sans-serif;font-weight:300;font-size:60px;color:var(--white);line-height:1}
.search-sub{left:393px;top:518px;font-family:"Raleway",sans-serif;font-size:19px;color:var(--white)}
.search-tabs{left:367px;top:562px;width:470px;height:34px;display:flex;background:#2a2d32}
.search-tabs span{flex:1;text-align:center;line-height:34px;font-size:14px;color:#aaa}
.search-tabs .on{color:var(--pink);border-top:2px solid var(--pink);background:#1a1c20;font-weight:600}
.search-field{left:367px;top:600px;width:358px;height:38px;background:var(--field);font-size:16px;color:#bbb;padding:9px 12px}
.search-btn{left:725px;top:600px;width:112px;height:38px;background:var(--pink);color:var(--white);font-size:18px;text-align:center;line-height:38px}

/* welcome */
.welcome-video{left:120px;top:858px;width:450px;height:252px;background:linear-gradient(90deg,#4a2e14,#3b2410)}
.play{left:310px;top:965px}
.welcome-title{left:626px;top:888px;font-family:"Raleway",sans-serif;font-weight:600;font-size:21px;color:var(--ink)}
.welcome-text{left:626px;top:916px;width:360px;font-size:13px;line-height:22px;color:var(--body)}
.read-more-btn{left:626px;top:1056px;height:20px;display:flex;font-size:11px;font-weight:600}
.read-more-btn b{background:var(--pink);color:var(--white);padding:0 8px;line-height:20px}
.read-more-btn i{width:22px;background:#333;color:#fff;font-style:normal;text-align:center;line-height:20px}

.videos-title{left:120px;top:1140px;font-family:"Raleway",sans-serif;font-weight:600;font-size:19px;color:var(--ink)}
.video-thumb{top:1198px;width:237px;height:142px}
.video-thumb .bar{position:absolute;left:0;bottom:0;width:100%;height:12px;background:#111}

/* agents */
.agents{left:0;top:1397px;width:1200px;height:378px;background:var(--navy)}
.agents-shape{left:640px;top:1397px;width:560px;height:378px;background:#212a35;clip-path:polygon(12% 0,100% 0,100% 100%,0 100%)}
.agent-photo{top:1493px;width:134px;height:134px;border-radius:50%;border:5px solid #2b333e;background:linear-gradient(180deg,#c9cdd2,#8d97a3)}
.agent-name{top:1503px;font-family:"Raleway",sans-serif;font-weight:700;font-size:19px;color:var(--white)}
.agent-role{top:1528px;font-size:13px;color:var(--muted)}
.badge-new{display:inline-block;margin-left:6px;background:#e0222f;color:#fff;font-size:9px;padding:0 5px;font-weight:600}
.agent-bio{top:1552px;width:272px;font-size:14px;line-height:22px;color:#e6e6e6}
.agent-link{top:1668px;font-size:14px;color:var(--pink)}
.arrow{width:22px;height:22px;border-radius:50%;display:flex;align-items:center;justify-content:center}
.arrow-dark{background:#232b36}
.arrow-solid{background:#1a1a1a}

/* testimonial */
.testimonial{left:0;top:1775px;width:1200px;height:376px;background:var(--light)}
.halo{left:262px;top:1825px;width:110px;height:110px;border-radius:50%;background:#d7d9dd}
.halo-low{left:104px;top:1980px;width:80px;height:80px;border-radius:50%;background:#d7d9dd}
.client-photo{left:140px;top:1843px;width:216px;height:216px;border-radius:50%;background:linear-gradient(135deg,#4a5868,#2a3440)}
.story-title{left:393px;top:1855px;background:var(--pink);color:var(--white);font-family:"Raleway",sans-serif;font-size:25px;padding:0 6px;line-height:34px}
.story-text{left:393px;top:1904px;width:630px;font-size:14.5px;line-height:24px;color:var(--ink)}
.story-link{left:393px;top:2047px;font-size:14px;color:var(--pink)}

/* app band */
.app-map{left:0;top:2151px;width:1200px;height:202px;background:linear-gradient(180deg,#e6e4df,#dcdad4)}
.app-phone{left:780px;top:2124px;width:104px;height:206px;border-radius:14px;background:linear-gradient(180deg,#2a2a2a,#111)}
.app-title{left:330px;top:2220px;background:var(--ink);color:var(--white);font-family:"Raleway",sans-serif;font-size:27px;padding:0 4px;line-height:32px}
.app-badge{left:645px;top:2258px;width:128px;height:36px;border-radius:5px;background:#111}

/* team */
.team-title{left:88px;top:2396px;background:var(--ink);color:var(--white);font-family:"Raleway",sans-serif;font-size:26px;padding:0 6px;line-height:34px}
.team-photo{top:2470px;width:132px;height:132px;border-radius:50%}

/* footer */
.site-footer{left:0;top:2700px;width:1200px;height:304px;background:var(--navy);border-top:4px solid var(--pink)}
.footer-brand{left:60px;top:2738px;font-family:"Raleway",sans-serif;font-weight:600;font-size:26px;color:var(--pink)}
.footer-address{left:60px;top:2818px;font-size:12.5px;line-height:19px;color:#d0d3d7}
.footer-social{left:60px;top:2932px;display:flex;gap:16px}
.footer-social span{width:11px;height:11px;background:#d0d3d7}
.footer-links{right:680px;top:2738px;text-align:right;font-size:12.5px;line-height:22.5px;color:#d0d3d7;font-family:"Raleway",sans-serif}
.footer-marker{left:540px;top:2740px;width:3px;height:18px;background:var(--pink)}
.field{left:582px;width:221px;background:var(--field);font-size:12px;color:#999;padding:6px 6px}
.quick-btn{left:582px;top:2924px;width:221px;height:34px;background:var(--pink);color:var(--white);font-family:"Raleway",sans-serif;font-weight:700;font-size:13px;text-align:center;line-height:34px}
.footer-map{left:827px;top:2736px;width:324px;height:160px;background:linear-gradient(135deg,#e9e7e1,#d6d5cf)}
.footer-map-label{left:827px;top:2900px;font-size:12.5px;color:#e6e6e6}
.bottom-bar{left:0;top:3004px;width:1200px;height:42px;background:var(--navy-deep);font-size:11.5px;color:#8a8f96}
.bottom-bar .copy{position:absolute;left:60px;top:13px}
.bottom-bar .privacy{position:absolute;right:60px;top:13px}
</style>
</head>
<body>

<!-- hero -->
<div class="abs hero" role="img" aria-label="Photo of a grey-shingled family house with a lush green lawn and trimmed hedges"></div>
<header class="abs site-header"></header>
<div class="abs brand">Brightkey Haven</div>
<nav class="abs main-nav">
  <span class="active">HOME</span><span>SEARCH</span><span>COMMUNITIES</span><span>BUYING A HOME</span><span>SELLING A HOME</span><span>CONTACT</span><span class="btn-login">LOGIN</span>
</nav>
<div class="abs header-social"><span></span><span></span><span></span></div>

<div class="abs search-panel"></div>
<div class="abs panel-social"><span></span><span></span><span></span></div>
<div class="abs search-title">Find Your Home</div>
<div class="abs search-sub">Bring to a whole source of homes for buy and sell</div>
<div class="abs search-tabs"><span class="on">BUY</span><span>Sell</span><span>All Homes</span></div>
<div class="abs search-field">Address, City, Zip</div>
<div class="abs search-btn">Search</div>

<!-- welcome -->
<div class="abs welcome-video" role="img" aria-label="Video still of an agent welcoming visitors"></div>
<svg class="abs play" width="70" height="50" viewBox="0 0 70 50"><rect width="70" height="50" rx="8" fill="rgba(0,0,0,.55)"/><path d="M28 15 L46 25 L28 35Z" fill="#fff"/></svg>
<h2 class="abs welcome-title">Welcome to Brightkey Haven</h2>
<p class="abs welcome-text">Welcome to Brightkey Haven. We are a full service real estate brokerage located in Ashford, New York offering personalized real estate solutions to the greater Ashford area. It is our goal, to ensure that every client we serve is fully represented in all of their real estate transactions.</p>
<div class="abs read-more-btn"><b>READ MORE</b><i>›</i></div>

<h3 class="abs videos-title">Our Videos</h3>
<div class="abs video-thumb" style="left:120px;background:linear-gradient(180deg,#9a9c9e,#7f8285)" role="img" aria-label="Client testimonial video"><div class="bar"></div></div>
<div class="abs video-thumb" style="left:367px;background:linear-gradient(180deg,#c9cbc8,#8f928f)" role="img" aria-label="Team meeting video"><div class="bar"></div></div>
<div class="abs video-thumb" style="left:615px;background:linear-gradient(180deg,#5a3618,#3c2410)" role="img" aria-label="Client testimonial video"><div class="bar"></div></div>
<div class="abs video-thumb" style="left:862px;background:linear-gradient(180deg,#9a9c9e,#7f8285)" role="img" aria-label="Client testimonial video"><div class="bar"></div></div>

<!-- agents -->
<section class="abs agents"></section>
<div class="abs agents-shape"></div>
<div class="abs arrow arrow-dark" style="left:54px;top:1579px"><svg width="8" height="10"><path d="M6 1 L2 5 L6 9" stroke="#ccc" stroke-width="1.5" fill="none"/></svg></div>
<div class="abs arrow arrow-dark" style="left:1128px;top:1579px"><svg width="8" height="10"><path d="M2 1 L6 5 L2 9" stroke="#ccc" stroke-width="1.5" fill="none"/></svg></div>

<div class="abs agent-photo" style="left:147px" role="img" aria-label="Portrait of agent Darren Holt"></div>
<div class="abs agent-name" style="left:292px">Darren Holt</div>
<div class="abs agent-role" style="left:292px">Real Estate Agent <span class="badge-new">NEW</span></div>
<p class="abs agent-bio" style="left:292px">Lorem ipsum dolor sit amet, consectetur adipiscing elit. Ut vitae erat eget metus suscipit fermentum. Vestibulum in enim id lacus malesuada maximus. Duis a aliquet sem. Sed enim risus, ultrices in</p>
<div class="abs agent-link" style="left:292px">Read More</div>

<div class="abs agent-photo" style="left:640px" role="img" aria-label="Portrait of agent Victor Lane"></div>
<div class="abs agent-name" style="left:786px">Victor Lane</div>
<div class="abs agent-role" style="left:786px">Real Estate Agent</div>
<p class="abs agent-bio" style="left:786px">Lorem ipsum dolor sit amet, consectetur adipiscing elit. Ut vitae erat eget metus suscipit fermentum. Vestibulum in enim id lacus malesuada maximus. Duis a aliquet sem. Sed enim risus, ultrices in</p>
<div class="abs agent-link" style="left:786px">Read More</div>

<!-- testimonial -->
<section class="abs testimonial"></section>
<div class="abs halo"></div>
<div class="abs halo-low"></div>
<div class="abs client-photo" role="img" aria-label="Photo of a happy new homeowner at the closing table"></div>
<div class="abs arrow arrow-solid" style="left:52px;top:1957px"><svg width="8" height="10"><path d="M6 1 L2 5 L6 9" stroke="#fff" stroke-width="1.5" fill="none"/></svg></div>
<div class="abs arrow arrow-solid" style="left:1128px;top:1957px"><svg width="8" height="10"><path d="M2 1 L6 5 L2 9" stroke="#fff" stroke-width="1.5" fill="none"/></svg></div>
<h2 class="abs story-title">Mira's New Home!</h2>
<p class="abs story-text">Mira is Brightkey Haven First Closing of the New Year! With clients like Mira we are sure to have a phenomenal year! Mira it has been a pleasure to work with and get to know you. From our first meeting when we walked through a leaning house :) then to the spooky (seemingly haunted ) house through all the other interesting but not quite right homes till now. We are proud to have traveled this journey with you and look forward to seeing you and your family prosper in your new home! Congratulations on your accomplishment!</p>
<div class="abs story-link">Read More</div>

<!-- app band -->
<div class="abs app-map" role="img" aria-label="Street map of the local area"></div>
<div class="abs app-phone" role="img" aria-label="Phone showing the home search app"></div>
<div class="abs app-title">Find Your Home with Our Mobile App</div>
<div class="abs app-badge"></div>

<!-- team -->
<h2 class="abs team-title">Meet our Team</h2>
<div class="abs team-photo" style="left:138px;background:linear-gradient(180deg,#5a3618,#3a2210)" role="img" aria-label="Team member portrait"></div>
<div class="abs team-photo" style="left:380px;background:linear-gradient(180deg,#6b4420,#3a2210)" role="img" aria-label="Team member portrait"></div>
<div class="abs team-photo" style="left:634px;background:linear-gradient(180deg,#9a9c9e,#6f6560)" role="img" aria-label="Team member portrait"></div>
<div class="abs team-photo" style="left:862px;background:linear-gradient(180deg,#b9b3ad,#8e7e72)" role="img" aria-label="Team member portrait"></div>

<!-- footer -->
<footer class="abs site-footer"></footer>
<div class="abs footer-brand">Brightkey Haven</div>
<address class="abs footer-address" style="font-style:normal">Brightkey Haven LLC<br>PO BOX 51830<br>Ashford, NY 10990<br>555 201.HOME(4663)<br>555 018.4470 (fax)</address>
<div class="abs footer-social"><span></span><span></span><span></span><span></span></div>
<nav class="abs footer-links">Home<br>About<br>Blog<br>Buying a Home<br>Selling a Home<br>Community<br>Contact<br>Services<br>Media<br>Careers<br>Organizations</nav>
<div class="abs footer-marker"></div>
<div class="abs field" style="top:2736px;height:30px">Name</div>
<div class="abs field" style="top:2782px;height:30px">Email</div>
<div class="abs field" style="top:2830px;height:76px">Subject</div>
<div class="abs quick-btn">QUICK CONTACT</div>
<div class="abs footer-map" role="img" aria-label="Map showing the office location"></div>
<svg class="abs" style="left:944px;top:2790px" width="18" height="26" viewBox="0 0 18 26"><path d="M9 0C4 0 0 4 0 9c0 7 9 17 9 17s9-10 9-17C18 4 14 0 9 0z" fill="#e0322f"/><circle cx="9" cy="9" r="3.5" fill="#fff"/></svg>
<div class="abs footer-map-label">Our Location</div>
<div class="abs bottom-bar"><span class="copy">Copyright © 2016 BrightkeyHaven</span><span class="privacy">Privacy Policy</span></div>

</body>
</html>
```